New Website - vostimo.net

This is what we looking for - http://www.craftlane-example.com/design/583017
Updates

hello, im back and i want some good designs for my website.. i need really creative ideas. this is for a cellphone provider company. Vostimo mobile please provide me a good ideas and i will go with u also to program the website

Font styles to use
Sans Serif

```html
<!DOCTYPE html>
<html lang="en">
<head>
<meta charset="utf-8">
<title>Vostimo Communications</title>
<link href="https://fonts.googleapis.com/css2?family=Open+Sans:wght@400;600&display=swap" rel="stylesheet">
<style>
:root{
  --ink:#3b3b3b;
  --muted:#5a5a5a;
  --blue:#1e8ad6;
  --nav-top:#7cc4f4;
  --nav-bottom:#45a4ea;
  --nav-active:#2a2a2a;
  --btn:#3a3a3a;
  --footer:#efefef;
  --bg-top:#000;
  --bg-bottom:#3a8ad0;
  --red:#a0141a;
}
*{box-sizing:border-box;margin:0;padding:0}
html,body{width:1104px;height:1200px;overflow:hidden}
body{font-family:"Open Sans",Arial,sans-serif;color:var(--ink);
  background:linear-gradient(180deg,var(--bg-top) 0,var(--bg-top) 130px,#0c1d2d 300px,#20588a 650px,var(--bg-bottom) 1200px)}
.site-header{width:922px;height:84px;margin:0 auto;display:flex;align-items:center;justify-content:space-between}
.brand{display:flex;align-items:center;gap:12px;color:#fff;padding-left:2px}
.brand-mark{width:34px;height:34px;border-radius:50%;background:var(--nav-bottom)}
.brand-name{font-size:36px;font-weight:400;letter-spacing:.5px;line-height:1}
.search{width:163px;height:30px;background:#fff;border:1px solid #ccc;display:flex;align-items:center;justify-content:space-between;padding:0 6px 0 11px;font-size:12px;color:#999}
.main-nav{height:46px;background:linear-gradient(180deg,var(--nav-top),var(--nav-bottom))}
.main-nav ul{width:922px;margin:0 auto;display:flex;list-style:none;height:46px}
.main-nav li{color:#fff;font-size:14px;white-space:nowrap;display:flex;align-items:center;justify-content:center;border-right:1px solid rgba(255,255,255,.35);text-transform:uppercase}
.main-nav li.active{background:var(--nav-active)}
.page{width:922px;margin:0 auto;background:#fff;height:1070px;position:relative}
.hero{position:absolute;left:12px;top:12px;width:898px;height:356px;background:linear-gradient(100deg,#e4e7ea 0,#f5f6f7 40%,#c9b79a 62%,#e9ecee 100%)}
.hero-text{position:absolute;left:12px;top:108px;font-size:20px;line-height:27px;color:#333;width:380px}
.cta{display:inline-block;margin-top:10px;background:linear-gradient(180deg,#5db6ee,#3196dc);color:#fff;font-size:17.5px;padding:7px 12px;border-radius:2px}
.dots{position:absolute;left:14px;top:326px;display:flex;gap:8px}
.dots span{width:13px;height:13px;border-radius:50%;background:#999}
.dots span:first-child{background:#333}
.welcome{position:absolute;left:14px;top:408px;width:662px}
.welcome h1{font-size:25px;font-weight:400;color:var(--blue);margin-bottom:6px}
.welcome p{font-size:12.5px;line-height:21px;color:var(--muted)}
.media{position:relative;background:linear-gradient(135deg,#3a3f45,#23272c 60%,#14171a)}
.play{position:absolute;left:50%;top:50%;transform:translate(-50%,-50%)}
.welcome-video{position:absolute;left:682px;top:409px;width:229px;height:143px}
.divider{position:absolute;left:0;right:0;top:581px;border-top:1px solid #ddd}
.features{position:absolute;left:12px;top:604px;display:flex;gap:17px}
.feature{width:288px}
.feature h2{font-size:25px;font-weight:400;color:var(--blue);line-height:30px}
.feature h3{font-size:14px;font-weight:600;color:#333;text-transform:uppercase;margin-bottom:9px}
.feature .media{height:134px}
.affordable-img{background:linear-gradient(160deg,#d9dde1,#f2f3f4 50%,#8d9297)}
.powerful-img{background:linear-gradient(135deg,#8a7a55,#3e4a58 50%,#6b7480)}
.flexible-img{background:linear-gradient(100deg,#cfd4d9,#eef0f2 45%,#3a3a3e 70%,#e3e5e7)}
.feature ul{list-style:none;margin-top:16px;height:121px}
.feature li{font-size:12.5px;line-height:16px;margin-bottom:9px;padding-left:22px;position:relative;color:#444;white-space:nowrap}
.feature li.wrap{white-space:normal}
.feature li svg{position:absolute;left:0;top:2px}
.feature li.highlight{color:var(--red)}
.number-check{display:flex;gap:11px;margin:-3px 0 8px 22px}
.number-check span{height:26px;background:#f2f2f2;border:1px solid #ddd;border-radius:2px}
.number-check .check{background:var(--btn);color:#fff;font-size:12.5px;padding:4px 9px;border-color:var(--btn)}
.btn{display:inline-block;background:var(--btn);color:#fff;font-size:13px;padding:6px 12px}
.site-footer{position:absolute;left:0;right:0;bottom:0;height:75px;background:var(--footer);padding:12px 13px;font-size:12px;color:#555}
.site-footer nav span{margin:0 10px}
.site-footer p{margin-top:12px}
.social{position:absolute;right:9px;top:22px;display:flex;gap:5px}
.social span{width:23px;height:23px;background:#3b5b9a;border-radius:2px}
.social span+span{background:#3fb4e8}
</style>
</head>
<body>
<header class="site-header">
  <div class="brand"><span class="brand-mark"></span><span class="brand-name">Vostimo</span></div>
  <div class="search">Search
    <svg width="17" height="17" viewBox="0 0 17 17"><circle cx="7" cy="7" r="5.5" fill="none" stroke="#888" stroke-width="2"/><path d="M11 11l5 5" stroke="#888" stroke-width="2.5"/></svg>
  </div>
</header>
<nav class="main-nav">
  <ul>
    <li class="active" style="width:81px">Home</li>
    <li style="width:121px">About Us</li>
    <li style="width:107px">Services</li>
    <li style="width:123px">Products</li>
    <li style="width:70px">FAQ</li>
    <li style="width:118px">Partners</li>
    <li style="width:135px">Contact Us</li>
    <li style="width:166px">Request a Quote</li>
  </ul>
</nav>
<main class="page">
  <section class="hero" role="img" aria-label="Smiling support agent wearing a headset in a bright office">
    <div class="hero-text">A revolutionary digital phone service that will save you, your family, and your business lots of money.<br><span class="cta">Get Started Now</span></div>
    <div class="dots"><span></span><span></span><span></span><span></span></div>
  </section>
  <section class="welcome">
    <h1>Welcome to Vostimo</h1>
    <p>Donec tincidunt consectetur nibh nec egestas. Donec placerat nulla lacus. Pellentesque habitant morbi tristique senectus et netus et malesuada fames ac turpis egestas. Duis pharetra lorem consequat fringilla porttitor. Curabitur in tellus ac quam blandit tristique. Aliquam erat volutpat. Nullam placerat orci eu pretium tincidunt. Curabitur sit amet venenatis est, sed volutpat turpis. Nunc tincidunt quis erat sit amet viverra. Nulla tincidunt libero augue, eu congue est fermentum id. Vivamus gravida erat sed diam vehicula, id euismod magna convallis. Vestibulum congue lectus massa, at eleifend velit mattis imperdiet.</p>
  </section>
  <div class="media welcome-video" role="img" aria-label="Video thumbnail of a businessman beside server racks">
    <svg class="play" width="56" height="56" viewBox="0 0 56 56"><circle cx="28" cy="28" r="25" fill="none" stroke="#fff" stroke-width="4"/><path d="M22 16l17 12-17 12z" fill="#fff"/></svg>
  </div>
  <div class="divider"></div>
  <section class="features">
    <article class="feature">
      <h2>Affordable</h2><h3>Start saving today!</h3>
      <div class="media affordable-img" role="img" aria-label="Hands dialing a desk phone"></div>
      <ul>
        <li><svg width="13" height="13" viewBox="0 0 13 13"><circle cx="6.5" cy="6.5" r="5.5" fill="none" stroke="#2b8fd8" stroke-width="1.6"/><path d="M4 6.5h5M6.5 4l2.5 2.5L6.5 9" fill="none" stroke="#2b8fd8" stroke-width="1.6"/></svg>Unlimited local and long distance calling</li>
        <li><svg width="13" height="13" viewBox="0 0 13 13"><circle cx="6.5" cy="6.5" r="5.5" fill="none" stroke="#2b8fd8" stroke-width="1.6"/><path d="M4 6.5h5M6.5 4l2.5 2.5L6.5 9" fill="none" stroke="#2b8fd8" stroke-width="1.6"/></svg>5 nation unlimited international</li>
        <li style="letter-spacing:-.2px"><svg width="13" height="13" viewBox="0 0 13 13"><circle cx="6.5" cy="6.5" r="5.5" fill="none" stroke="#2b8fd8" stroke-width="1.6"/><path d="M4 6.5h5M6.5 4l2.5 2.5L6.5 9" fill="none" stroke="#2b8fd8" stroke-width="1.6"/></svg>No set-up, equipment fees, or hidden charges</li>
        <li><svg width="13" height="13" viewBox="0 0 13 13"><circle cx="6.5" cy="6.5" r="5.5" fill="none" stroke="#2b8fd8" stroke-width="1.6"/><path d="M4 6.5h5M6.5 4l2.5 2.5L6.5 9" fill="none" stroke="#2b8fd8" stroke-width="1.6"/></svg>No contracts or commitments</li>
      </ul>
      <span class="btn">COMPARE RATE AND PLANS</span>
    </article>
    <article class="feature">
      <h2>Powerful</h2><h3>Incredible features, standard</h3>
      <div class="media powerful-img" role="img" aria-label="Video thumbnail of a glowing network of connected people">
        <svg class="play" width="64" height="64" viewBox="0 0 56 56"><circle cx="28" cy="28" r="25" fill="none" stroke="#fff" stroke-width="4"/><path d="M22 16l17 12-17 12z" fill="#fff"/></svg>
      </div>
      <ul>
        <li><svg width="13" height="13" viewBox="0 0 13 13"><circle cx="6.5" cy="6.5" r="5.5" fill="none" stroke="#2b8fd8" stroke-width="1.6"/><path d="M4 6.5h5M6.5 4l2.5 2.5L6.5 9" fill="none" stroke="#2b8fd8" stroke-width="1.6"/></svg>Seamless integration with Mailora</li>
        <li><svg width="13" height="13" viewBox="0 0 13 13"><circle cx="6.5" cy="6.5" r="5.5" fill="none" stroke="#2b8fd8" stroke-width="1.6"/><path d="M4 6.5h5M6.5 4l2.5 2.5L6.5 9" fill="none" stroke="#2b8fd8" stroke-width="1.6"/></svg>Get calls and voicemail anywhere</li>
        <li><svg width="13" height="13" viewBox="0 0 13 13"><circle cx="6.5" cy="6.5" r="5.5" fill="none" stroke="#2b8fd8" stroke-width="1.6"/><path d="M4 6.5h5M6.5 4l2.5 2.5L6.5 9" fill="none" stroke="#2b8fd8" stroke-width="1.6"/></svg>100% hurrican proof</li>
        <li class="highlight"><svg width="13" height="13" viewBox="0 0 13 13"><circle cx="6.5" cy="6.5" r="5.5" fill="none" stroke="#2b8fd8" stroke-width="1.6"/><path d="M4 6.5h5M6.5 4l2.5 2.5L6.5 9" fill="none" stroke="#2b8fd8" stroke-width="1.6"/></svg>Featuring the Power of Callnexa!</li>
      </ul>
      <span class="btn">TAKE THE TOUR</span>
    </article>
    <article class="feature">
      <h2>Flexible</h2><h3>Service on your own terms</h3>
      <div class="media flexible-img" role="img" aria-label="Businesswoman on a mobile phone holding a tablet"></div>
      <ul>
        <li><svg width="13" height="13" viewBox="0 0 13 13"><circle cx="6.5" cy="6.5" r="5.5" fill="none" stroke="#2b8fd8" stroke-width="1.6"/><path d="M4 6.5h5M6.5 4l2.5 2.5L6.5 9" fill="none" stroke="#2b8fd8" stroke-width="1.6"/></svg>Keep your Number!</li>
        <li class="number-check" style="padding:0"><span style="width:58px"></span><span style="width:58px"></span><span style="width:79px"></span><span class="check">Check</span></li>
        <li><svg width="13" height="13" viewBox="0 0 13 13"><circle cx="6.5" cy="6.5" r="5.5" fill="none" stroke="#2b8fd8" stroke-width="1.6"/><path d="M4 6.5h5M6.5 4l2.5 2.5L6.5 9" fill="none" stroke="#2b8fd8" stroke-width="1.6"/></svg>Choose your own area code</li>
        <li class="wrap"><svg width="13" height="13" viewBox="0 0 13 13"><circle cx="6.5" cy="6.5" r="5.5" fill="none" stroke="#2b8fd8" stroke-width="1.6"/><path d="M4 6.5h5M6.5 4l2.5 2.5L6.5 9" fill="none" stroke="#2b8fd8" stroke-width="1.6"/></svg>Custom-tailored business solutions, both hosted local</li>
      </ul>
      <span class="btn">LEARN HOW IT WORKS</span>
    </article>
  </section>
  <footer class="site-footer">
    <nav>Home<span>|</span>About us<span>|</span>Services<span>|</span>Products<span>|</span>FAQ<span>|</span>Partners<span>|</span>Contact us<span>|</span>Request a Quote</nav>
    <p>Copyright &copy; 2014 &nbsp;Vostimo Communications. &nbsp;All rights reserved</p>
    <div class="social"><span></span><span></span></div>
  </footer>
</main>
</body>
</html>
```